Fahrzeugbeschriftung für Zahnarztpraxis
Zielgruppe
Zahnarztpraxis. Das jetzige Logo ist bereits von grafikmarkt
Aufgabenstellung
Bestandslogo und dieses Grün verwenden . ( ist von Euch ) . Damals wurde ein Wettbewerb von der Zahnarztpraxis ausgeschrieben . Adresse und Kontaktdaten sollten hervorgehoben werde.
Lustig mit Wiedererkennungseffekt ( Zahnfee muss nicht sein ) die zukünftigen Folien sollten auf die Flächen und die veloran stimmig passen

```html
<!DOCTYPE html>
<html lang="de">
<head>
<meta charset="utf-8">
<title>Fahrzeugbeschriftung – LUMEN Zahnärzte</title>
<link href="https://fonts.googleapis.com/css2?family=Ubuntu+Condensed&family=Ubuntu:wght@500&display=swap" rel="stylesheet">
<style>
  :root {
    --canvas-bg: #eef0f0;
    --panel-white: #ffffff;
    --panel-edge: #d9dcdf;
    --rib: #eceef0;
    --brand-grey: #6a717c;
    --brand-green: #3e6a1e;
    --brand-lime: #b7d12e;
    --lime-light: #d6e36a;
    --band-dark: #1d2410;
    --band-text: #c9e03a;
    --text-dark: #3a3f45;
    --fairy-sky: #d6ecf7;
    --fairy-green: #7dbb3a;
  }
  * { margin: 0; padding: 0; box-sizing: border-box; }
  html, body { width: 1200px; height: 900px; overflow: hidden; }
  body {
    background: var(--canvas-bg);
    font-family: "Ubuntu Condensed", "Arial Narrow", sans-serif;
    color: var(--text-dark);
    position: relative;
  }

  /* cargo box side panel */
  .box-panel {
    position: absolute; left: 60px; top: 165px;
    width: 660px; height: 570px;
    background: var(--panel-white);
    border: 1px solid var(--panel-edge);
    border-radius: 14px 10px 6px 6px;
    overflow: hidden;
  }
  .box-panel .ribs {
    position: absolute; inset: 60px 30px 70px 30px;
    background: repeating-linear-gradient(to bottom, transparent 0 38px, var(--rib) 38px 44px);
  }
  .web-line {
    position: absolute; top: 16px; right: 32px;
    font-size: 32px; color: var(--text-dark);
    display: flex; align-items: center; gap: 6px;
    white-space: nowrap;
  }
  .mascot-area {
    position: absolute; left: 0; top: 30px;
    width: 210px; height: 460px;
    background: linear-gradient(160deg, var(--lime-light) 0%, var(--brand-lime) 45%, #9aa2ab 100%);
    border-radius: 0 60% 60% 0 / 0 50% 50% 0;
    opacity: .9;
  }
  .brand-name {
    position: absolute; right: 32px; top: 105px;
    font-family: "Ubuntu", sans-serif; font-weight: 500;
    text-align: right;
    line-height: 1;
    white-space: nowrap;
  }
  .brand-name .word { display: block; font-size: 96px; letter-spacing: 2px; color: var(--brand-grey); }
  .brand-name .sub {
    display: block; font-size: 48px; letter-spacing: 3px; margin-top: 8px;
    font-family: "Ubuntu Condensed", "Arial Narrow", sans-serif; font-weight: 400;
    color: var(--brand-green);
  }
  .doctors {
    position: absolute; right: 32px; top: 318px;
    display: flex; font-size: 22px; color: var(--text-dark);
    white-space: nowrap;
  }
  .doctor { padding: 0 12px; text-align: right; }
  .doctor:last-child { padding-right: 0; }
  .doctor + .doctor { border-left: 1.5px solid var(--text-dark); text-align: left; }
  .doctor .title { color: var(--brand-grey); display: block; margin-bottom: 16px; }
  .email-line {
    position: absolute; right: 32px; bottom: 78px;
    font-size: 24px; display: flex; align-items: center; gap: 6px;
    white-space: nowrap;
  }
  .address-band {
    position: absolute; left: 30px; right: 0; bottom: 0; height: 44px;
    background: var(--band-dark);
    border-radius: 6px 6px 0 0;
    color: var(--band-text);
    font-size: 25px;
    display: flex; align-items: center; justify-content: center; gap: 6px;
    white-space: nowrap;
  }

  /* cab door panel */
  .door-panel {
    position: absolute; left: 800px; top: 305px;
    width: 330px; height: 430px;
    background: var(--panel-white);
    border: 1px solid var(--panel-edge);
    border-radius: 10px 10px 6px 6px;
    overflow: hidden;
  }
  .fairy-area {
    position: absolute; left: 40px; top: 20px;
    width: 250px; height: 300px;
    background: radial-gradient(ellipse at 55% 40%, #f3e08a 0%, var(--fairy-green) 45%, var(--fairy-sky) 80%);
    border-radius: 46% 46% 40% 40%;
  }
  .phone-band {
    position: absolute; left: 0; right: 0; bottom: 0; height: 72px;
    background: var(--band-dark);
    color: var(--band-text);
    font-size: 30px;
    display: flex; align-items: center; justify-content: center; gap: 10px;
    white-space: nowrap;
  }
  .icon { flex: none; }
</style>
</head>
<body>

  <section class="box-panel">
    <div class="ribs"></div>

    <div class="web-line">
      <svg class="icon" width="28" height="28" viewBox="0 0 24 24" fill="none" stroke="#3e6a1e" stroke-width="1.6">
        <circle cx="12" cy="12" r="10"/><ellipse cx="12" cy="12" rx="4.5" ry="10"/><line x1="2" y1="12" x2="22" y2="12"/><line x1="4" y1="7" x2="20" y2="7"/><line x1="4" y1="17" x2="20" y2="17"/>
      </svg>
      <span>www.zahn-lumen.de</span>
    </div>

    <div class="mascot-area" role="img" aria-label="Illustration: grünes Maskottchen der Praxis, das sich um einen grauen Bogen windet"></div>

    <div class="brand-name">
      <span class="word">LUMEN</span>
      <span class="sub">ZAHNÄRZTE</span>
    </div>

    <div class="doctors">
      <div class="doctor"><span class="title">DR. MED. DENT.</span>KONRAD VELTEN</div>
      <div class="doctor"><span class="title">DR. MED. DENT.</span>MATTHIAS RODER</div>
    </div>

    <div class="email-line">
      <svg class="icon" width="24" height="24" viewBox="0 0 24 24" fill="none" stroke="#3e6a1e" stroke-width="1.6">
        <path d="M2 11 L22 3 L15 21 L11 13 Z"/><line x1="11" y1="13" x2="22" y2="3"/>
      </svg>
      <span>praxis@zahn-lumen.de</span>
    </div>

    <div class="address-band">
      <svg class="icon" width="22" height="22" viewBox="0 0 24 24" fill="none" stroke="#c9e03a" stroke-width="1.6">
        <path d="M12 22 C6 15 4 12 4 9 a8 8 0 0 1 16 0 c0 3 -2 6 -8 13z"/><circle cx="12" cy="9" r="3"/>
      </svg>
      <span>Lindenhofstr. 14 • 66119 Talberg</span>
    </div>
  </section>

  <section class="door-panel">
    <div class="fairy-area" role="img" aria-label="Illustration: Zahnfee im grünen Kleid mit Krone und Flügeln, die einen Zahn hält, mit dem Schriftzug „Wir sind jeden Tag für Sie da“"></div>

    <div class="phone-band">
      <svg class="icon" width="32" height="32" viewBox="0 0 24 24" fill="none" stroke="#ffffff" stroke-width="1.5">
        <path d="M5 3 h4 l2 5 -2.5 1.5 a11 11 0 0 0 6 6 L16 13 l5 2 v4 a2 2 0 0 1 -2 2 A16 16 0 0 1 3 5 a2 2 0 0 1 2 -2z"/>
        <path d="M14 3 a7 7 0 0 1 7 7"/><path d="M14 6.5 a3.5 3.5 0 0 1 3.5 3.5"/>
      </svg>
      <span>(01234) 56 78 90</span>
    </div>
  </section>

</body>
</html>
```